Business Card Design Project - Sports Brand

Lumora is a e-commerce fitness wear brand for ladies who are into gym, pole and swim.

Card should not be overly cluttered and should include the following:

1. logo
2. Name of the company (Use "Lumora Wear Pte Ltd" for now)
3. Address of company (Use a mock address)
4. Representative's name and contact info etc. (use a mock name and contact info)
5. website address

Target Market(s)

Women who are into pole , gym, and swim.

Women who shop online

Industry/Entity Type

E-Commerce

Colors

Designer to choose colors to be used in the design.

Requirements
Nice to have
• feminine sublimation of colours

Need not be printed on traditional paper. We would like the design to be revolutionary and interesting to the eye :)
Should not have
• the design should not be traditional looking. Do not include illustrations of Bikinis, yoga poses etc. in the card.

```html
<!DOCTYPE html>
<html lang="en">
<head>
<meta charset="utf-8">
<title>Lumora Wear – Business Card</title>
<link href="https://fonts.googleapis.com/css2?family=Crimson+Text:wght@400;600&display=swap" rel="stylesheet">
<style>
  :root {
    --backdrop: #2a2a2a;
    --card: #ffffff;
    --brand-red: #b8242f;
    --brand-pink: #e0448a;
    --brand-coral: #ec5a3c;
    --ink: #3a3a3a;
    --ink-soft: #555555;
  }
  * { margin: 0; padding: 0; box-sizing: border-box; }
  html, body {
    width: 1200px; height: 900px; overflow: hidden;
    background: var(--backdrop);
    font-family: "Crimson Text", Georgia, serif;
  }
  .canvas { position: relative; width: 1200px; height: 900px; }
  .card {
    position: absolute; width: 620px; height: 354px;
    background: var(--card);
    box-shadow: 0 10px 30px rgba(0,0,0,.45);
    overflow: hidden;
  }
  .card--front { left: 70px; top: 80px; }
  .card--back { left: 510px; top: 466px; }

  .brand-disc {
    position: absolute; border-radius: 50%;
    background: radial-gradient(circle at 60% 65%, var(--brand-coral), var(--brand-pink) 85%);
  }
  .card--front .brand-disc { width: 210px; height: 210px; left: 120px; top: 66px; }
  .brand-name {
    position: absolute; left: 350px; top: 104px;
    font-size: 64px; font-weight: 600; line-height: 1;
    color: var(--brand-red);
    white-space: nowrap;
  }
  .brand-tagline {
    position: absolute; left: 354px; top: 184px;
    font-size: 24px; line-height: 1; color: var(--ink);
    white-space: nowrap;
  }

  .card--back .brand-disc { width: 250px; height: 250px; left: 50px; top: 52px; }
  .card--back .brand-name {
    left: 50px; top: 150px; width: 250px; text-align: center;
    font-size: 50px; color: var(--card);
  }

  .contact {
    position: absolute; right: 34px; top: 34px;
    text-align: right; color: var(--ink);
  }
  .contact__name { font-size: 24px; letter-spacing: 1px; color: var(--brand-pink); line-height: 1.1; }
  .contact__role { font-size: 18px; color: var(--ink-soft); margin-bottom: 24px; }
  .contact__list { list-style: none; font-size: 17px; }
  .contact__item {
    display: flex; justify-content: flex-end; align-items: center;
    gap: 10px; height: 30px; white-space: nowrap;
  }
  .contact__icon { width: 22px; height: 22px; flex: none; }
  .company { margin-top: 26px; }
  .company__name { font-size: 21px; letter-spacing: .5px; color: var(--brand-pink); line-height: 1.1; white-space: nowrap; }
  .company__address { font-size: 17px; color: var(--ink); line-height: 1.25; }
</style>
</head>
<body>
<main class="canvas">

  <section class="card card--front">
    <div class="brand-disc"></div>
    <div class="brand-name">Lumora</div>
    <div class="brand-tagline">Yoga•Swim•Pole</div>
  </section>

  <section class="card card--back">
    <div class="brand-disc"></div>
    <div class="brand-name">Lumora</div>

    <div class="contact">
      <div class="contact__name">MARA ELLISON</div>
      <div class="contact__role">Director</div>
      <ul class="contact__list">
        <li class="contact__item">555 014 2290
          <svg class="contact__icon" viewBox="0 0 22 22" aria-hidden="true">
            <circle cx="11" cy="11" r="11" fill="#e0448a"/>
            <path d="M7.5 6c.6-.4 1.2-.3 1.5.2l.9 1.6c.3.5.1 1-.3 1.3l-.6.4c.5 1.2 1.4 2.1 2.6 2.7l.5-.6c.3-.4.9-.5 1.3-.2l1.6 1c.5.3.5 1 .1 1.5-.8.9-1.9 1.2-3 .6C9.8 13.4 8.3 11.9 7.2 9.6c-.5-1.1-.5-2.6.3-3.6z" fill="#fff"/>
          </svg>
        </li>
        <li class="contact__item">mara@lumorawear.com
          <svg class="contact__icon" viewBox="0 0 22 22" aria-hidden="true">
            <circle cx="11" cy="11" r="11" fill="#e0448a"/>
            <rect x="5.5" y="7" width="11" height="8" rx="1" fill="#fff"/>
            <path d="M5.8 7.4 11 11.4l5.2-4" fill="none" stroke="#e0448a" stroke-width="1"/>
          </svg>
        </li>
        <li class="contact__item">www.lumorawear.com
          <svg class="contact__icon" viewBox="0 0 22 22" aria-hidden="true">
            <circle cx="11" cy="11" r="11" fill="#e0448a"/>
            <g fill="none" stroke="#fff" stroke-width="1.1">
              <circle cx="11" cy="11" r="5.5"/>
              <ellipse cx="11" cy="11" rx="2.4" ry="5.5"/>
              <path d="M5.5 11h11M6.3 8h9.4M6.3 14h9.4"/>
            </g>
          </svg>
        </li>
      </ul>
      <div class="company">
        <div class="company__name">LUMORA WEAR PTE. LTD.</div>
        <div class="company__address">Shop 12, Orchid Lane<br>Singapore 408800</div>
      </div>
    </div>
  </section>

</main>
</body>
</html>
```